Business Card Design for Mortgage Broking Business

We need to redesign the business card. Mortgage broking business, doing home loan and commercial loans, existing logo, also QLPN member logo. design style needs to be simple, professional, elegant.

once final, need to setup for a team of different names and contact details.

Industry/Entity Type

Loan

Contact Information for Business Card

Name; Mobile; Email; Address; Tel; Fax; Australian Credit Licence: 782316

```html
<!DOCTYPE html>
<html lang="en">
<head>
<meta charset="utf-8">
<title>Northgate Home Finance – Business Card</title>
<link rel="stylesheet" href="https://fonts.googleapis.com/css2?family=Open+Sans:wght@400;600;700&display=swap">
<style>
  :root {
    --navy: #1f2d86;
    --sky: #2a9ee2;
    --sky-light: #4cb4ef;
    --lime: #7cc242;
    --white: #ffffff;
    --backdrop: #e6e6e6;
    --ink-soft: #2c3d8f;
  }
  * { box-sizing: border-box; margin: 0; padding: 0; }
  html, body { width: 1200px; height: 852px; overflow: hidden; }
  body {
    background: var(--backdrop);
    font-family: "Open Sans", Arial, sans-serif;
    position: relative;
  }
  .card {
    position: absolute;
    top: 276px;
    width: 520px;
    height: 300px;
    border-radius: 22px;
    overflow: hidden;
    box-shadow: 0 6px 18px rgba(0,0,0,0.18);
  }

  /* Brand lockup */
  .brand { position: absolute; display: flex; align-items: flex-start; gap: 10px; }
  .brand-mark { width: 26px; height: 26px; background: var(--lime); flex: none; margin-top: 6px; }
  .brand-name { font-weight: 700; font-size: 22px; line-height: 26px; color: var(--navy); }
  .brand-tag { font-weight: 700; font-size: 14px; line-height: 20px; color: var(--navy); margin-top: 2px; }

  /* Back of card */
  .card-back { left: 50px; background: var(--navy); }
  .card-back .brand { left: 64px; top: 84px; }
  .card-back .brand-name { color: var(--white); }
  .card-back .brand-tag { color: var(--sky-light); }
  .info-band {
    position: absolute; left: 0; right: 0; bottom: 0; height: 82px;
    background: var(--sky);
    color: var(--white);
    text-align: center;
    padding-top: 16px;
    font-size: 15px;
    line-height: 24px;
  }

  /* Front of card */
  .card-front { left: 630px; background: var(--white); }
  .waves { position: absolute; inset: 0; }
  .card-front .brand { left: 36px; top: 78px; }
  .member-badge {
    position: absolute; right: 26px; top: 14px;
    width: 104px; height: 28px;
    border: 2px solid var(--navy);
    background: var(--white);
  }
  .person { position: absolute; left: 36px; top: 170px; }
  .person-name { font-weight: 700; font-size: 19px; line-height: 24px; color: var(--navy); }
  .person-role { font-size: 13px; line-height: 18px; color: var(--ink-soft); }
  .contact-list {
    position: absolute; right: 22px; top: 110px;
    list-style: none; color: var(--white);
    font-size: 12px; line-height: 21px; text-align: right;
  }
  .contact-list li { display: flex; justify-content: flex-end; align-items: center; gap: 8px; }
  .contact-list svg { width: 12px; height: 12px; flex: none; }
</style>
</head>
<body>

<section class="card card-back" aria-label="Business card back">
  <div class="brand">
    <span class="brand-mark"></span>
    <div>
      <div class="brand-name">Northgate<br>Home Finance</div>
      <div class="brand-tag">Lending Partners</div>
    </div>
  </div>
  <div class="info-band">
    <p>Personal, Residential, Commercial, Plan &amp; Equipment Finance</p>
    <p>Australian Credit Licence: 782316</p>
  </div>
</section>

<section class="card card-front" aria-label="Business card front">
  <svg class="waves" viewBox="0 0 520 300" aria-hidden="true">
    <defs>
      <path id="wave-edge" d="M520 72 C400 80 330 110 300 170 C270 240 150 270 0 280"/>
    </defs>
    <use href="#wave-edge" transform="translate(-22,-26)" fill="none" stroke="var(--lime)" stroke-width="5"/>
    <path d="M520 72 C400 80 330 110 300 170 C270 240 150 270 0 280 L0 360 L560 360 L560 72 Z" transform="translate(-11,-13)" fill="var(--sky)"/>
    <path d="M520 72 C400 80 330 110 300 170 C270 240 150 270 0 280 L0 360 L560 360 L560 72 Z" transform="translate(-4,-5)" fill="var(--white)"/>
    <path d="M520 72 C400 80 330 110 300 170 C270 240 150 270 0 280 L0 360 L560 360 L560 72 Z" fill="var(--navy)"/>
  </svg>

  <div class="member-badge" role="img" aria-label="Member badge"></div>

  <div class="brand">
    <span class="brand-mark"></span>
    <div>
      <div class="brand-name">Northgate<br>Home Finance</div>
      <div class="brand-tag">Lending Partners</div>
    </div>
  </div>

  <div class="person">
    <div class="person-name">Your Long Name</div>
    <div class="person-role">Managing Director</div>
  </div>

  <ul class="contact-list">
    <li>00.00.00.0000
      <svg viewBox="0 0 12 12"><path d="M2 1h3l1 3-2 1a7 7 0 0 0 3 3l1-2 3 1v3c-6 0-10-4-10-10z" fill="#fff"/></svg></li>
    <li>00.00.00.0000
      <svg viewBox="0 0 12 12"><rect x="3" y="1" width="6" height="3" fill="#fff"/><rect x="1" y="4" width="10" height="5" rx="1" fill="#fff"/><rect x="3" y="8" width="6" height="3" fill="#fff" stroke="var(--navy)" stroke-width=".6"/></svg></li>
    <li>www.yourwebsite.com
      <svg viewBox="0 0 12 12"><circle cx="6" cy="6" r="5" fill="none" stroke="#fff" stroke-width="1.2"/><ellipse cx="6" cy="6" rx="2" ry="5" fill="none" stroke="#fff"/><line x1="1" y1="6" x2="11" y2="6" stroke="#fff"/></svg></li>
    <li>yourname@yourwebsite.com
      <svg viewBox="0 0 12 12"><rect x="1" y="2.5" width="10" height="7" fill="#fff"/><path d="M1 2.5l5 4 5-4" fill="none" stroke="var(--navy)"/></svg></li>
    <li>Your Commercial or office address
      <svg viewBox="0 0 12 12"><path d="M6 11C3 7 2.5 5.5 2.5 4.5a3.5 3.5 0 0 1 7 0c0 1-.5 2.5-3.5 6.5z" fill="#fff"/><circle cx="6" cy="4.5" r="1.2" fill="var(--navy)"/></svg></li>
  </ul>
</section>

</body>
</html>
```